Commercial and Multifamily informational website

We need a website for our commercial real estate management company. We will manage offices, retail, apartments and others. Here is the brief verbiage: Providing quality commercial and multifamily portfolio management to Landlords, REITs, and financial institutions. 

Industry/Entity Type

Real Estate

Number of Pages Required

2 page

Font styles to use
Sans Serif
Other font styles liked:
• Muli, Garamond

Colors
0555a3
5c5c5c
3176b5
85acd3
474747

Requirements
Must have
• Home page and contact page

```html
<!DOCTYPE html>
<html lang="en">
<head>
<meta charset="utf-8">
<title>Harlow Real Estate Management</title>
<link rel="stylesheet" href="https://fonts.googleapis.com/css2?family=Lato:wght@400;700;900&family=Open+Sans:wght@400;600;700&family=Oswald:wght@400&family=Roboto:wght@400;500&display=swap">
<style>
:root{
  --brand:#0555a3;
  --blue:#3176b5;
  --sky:#85acd3;
  --ink:#474747;
  --grey:#5c5c5c;
  --dark:#2b2d30;
  --soft:#f2f2f2;
  --foot:#f1f4f8;
  --white:#ffffff;
}
*{box-sizing:border-box;margin:0;padding:0}
html,body{width:1200px;height:2970px;overflow:hidden;background:var(--white)}
body{position:relative;font-family:"Open Sans",Arial,sans-serif;color:var(--ink)}
.abs{position:absolute}

/* header */
.site-header{position:absolute;left:0;top:0;width:1200px;height:130px;background:var(--white)}
.brand{position:absolute;left:100px;top:34px;display:flex;align-items:center;gap:12px}
.brand-mark{width:18px;height:18px;background:var(--brand)}
.brand-name{font-family:"Lato",sans-serif;font-weight:900;font-size:30px;color:var(--brand);letter-spacing:1px}
.top-contact{position:absolute;right:48px;top:18px;display:flex;gap:26px;align-items:center;font-family:"Roboto",sans-serif;font-size:16px}
.top-contact span{display:flex;align-items:center;gap:10px}
.top-contact .mail{color:var(--blue)}
.top-contact .phone{color:var(--ink)}
.dot-icon{width:32px;height:32px;border-radius:50%;display:flex;align-items:center;justify-content:center}
.dot-icon.blue{background:var(--blue)}
.dot-icon.dark{background:var(--ink)}
.main-nav{position:absolute;left:378px;top:76px;width:822px;height:54px;background:var(--blue);clip-path:polygon(30px 0,100% 0,100% 100%,0 100%)}
.main-nav ul{list-style:none;display:flex;position:absolute;left:82px;top:0;height:54px;align-items:center;gap:0}
.main-nav li{font-family:"Roboto",sans-serif;font-size:15px;color:var(--white);text-transform:uppercase;margin-right:50px}

/* hero */
.hero{position:absolute;left:0;top:130px;width:1200px;height:540px;background:linear-gradient(180deg,#3a2a20 0%,#6a5244 40%,#8a7466 70%,#4d3b30 100%)}
.hero-title{position:absolute;left:0;width:1200px;top:120px;text-align:center;font-family:"Open Sans",sans-serif;font-weight:600;font-size:41px;color:var(--white);letter-spacing:.5px}
.hero-sub{position:absolute;left:200px;width:800px;top:206px;text-align:center;font-weight:700;font-size:17px;line-height:30px;color:var(--white)}
.hero-btn{position:absolute;left:527px;top:312px;width:148px;height:52px;border:2px solid var(--white);color:var(--white);font-family:"Roboto",sans-serif;font-size:16px;display:flex;align-items:center;justify-content:center;text-transform:uppercase}
.hero-arrow{position:absolute;top:240px}

/* category panels */
.cat-shadow{position:absolute;left:140px;top:960px;width:920px;height:50px;border-radius:50%;background:radial-gradient(ellipse at center,rgba(0,0,0,.22),rgba(0,0,0,0) 70%)}
.cat{position:absolute;top:576px;width:334px;height:414px;color:var(--white)}
.cat.offices{left:100px;background:var(--blue);clip-path:polygon(0 0,100% 0,100% 100%,0 94%)}
.cat.retail{left:433px;background:var(--dark)}
.cat.apartments{left:766px;width:334px;background:var(--sky);clip-path:polygon(0 0,100% 0,100% 94%,0 100%);border-top:4px solid var(--white)}
.cat h3{position:absolute;left:16px;top:16px;font-family:"Oswald",sans-serif;font-weight:400;font-size:29px}
.cat p{position:absolute;left:18px;top:64px;width:300px;font-size:12px;line-height:22px;color:rgba(255,255,255,.85)}
.cat .photo{position:absolute;left:16px;top:144px;width:302px;height:186px}

/* about */
.section-title{position:absolute;left:0;width:1200px;text-align:center;font-family:"Lato",sans-serif;font-weight:700;font-size:29px;color:var(--blue);text-transform:uppercase}
.rule{position:absolute;height:2px;background:var(--blue)}
.about-text{position:absolute;left:150px;width:900px;top:1136px;text-align:center;font-size:12.5px;line-height:22px;color:var(--ink)}
.stats{position:absolute;left:60px;top:1250px;width:1080px;display:flex}
.stat{flex:1;text-align:center;position:relative}
.stat + .stat::before{content:"";position:absolute;left:0;top:10px;width:1px;height:80px;background:#cfcfcf}
.stat svg{display:block;margin:0 auto 18px}
.stat .label{font-family:"Roboto",sans-serif;font-size:15px;color:var(--ink);text-transform:uppercase}
.stat .value{font-family:"Roboto",sans-serif;font-size:21px;color:var(--ink);margin-top:8px}

/* services */
.services{position:absolute;left:0;top:1450px;width:1200px;height:530px;background:var(--soft)}
.services .photo{position:absolute;left:0;top:0;width:564px;height:530px;background:linear-gradient(160deg,#d9dad8 0%,#8b8d8f 35%,#3e3f42 60%,#9a9a98 100%)}
.services h2{position:absolute;left:627px;top:44px;font-family:"Lato",sans-serif;font-weight:700;font-size:26px;color:var(--blue)}
.services .srule{position:absolute;left:627px;top:84px;width:134px;height:2px;background:var(--blue)}
.services .intro{position:absolute;left:627px;top:108px;width:530px;font-size:12.5px;line-height:22px}
.service{position:absolute;width:240px}
.service h4{font-family:"Roboto",sans-serif;font-weight:500;font-size:16px;color:var(--ink);margin-top:10px}
.service p{font-size:12px;line-height:22px;margin-top:6px}

/* blog */
.post{position:absolute;top:2150px;width:312px;height:402px;background:var(--white);box-shadow:0 2px 8px rgba(0,0,0,.18)}
.post .photo{width:312px;height:196px}
.post h3{margin-top:20px;text-align:center;font-family:"Open Sans",sans-serif;font-weight:600;font-size:18px}
.post h3.accent{color:var(--brand)}
.post p{margin:14px auto 0;width:270px;text-align:center;font-size:12px;line-height:22px}
.post .btn{display:flex;margin:14px auto 0;width:120px;height:36px;align-items:center;justify-content:center;font-family:"Roboto",sans-serif;font-size:12px;text-transform:uppercase;border:1px solid #bfbfbf;color:var(--grey)}
.post .btn.solid{background:var(--blue);border-color:var(--blue);color:var(--white)}

/* footer */
.site-footer{position:absolute;left:0;top:2598px;width:1200px;height:372px;background:var(--foot)}
.foot-brand{position:absolute;left:0;width:1200px;top:52px;display:flex;justify-content:center;align-items:center;gap:12px}
.foot-contact{position:absolute;left:0;width:1200px;top:166px;display:flex;justify-content:center;gap:22px;font-family:"Roboto",sans-serif;font-size:19px;color:var(--ink)}
.foot-contact span{display:flex;align-items:center;gap:12px}
.ring{width:34px;height:34px;border:2px solid var(--ink);border-radius:50%;display:flex;align-items:center;justify-content:center}
.foot-nav{position:absolute;left:0;width:1200px;top:240px;display:flex;justify-content:center;list-style:none;font-family:"Roboto",sans-serif;font-size:15px;color:#111;text-transform:uppercase}
.foot-nav li+li::before{content:"|";margin:0 28px}
.foot-line{position:absolute;left:100px;top:298px;width:1000px;height:2px;background:#444}
.copyright{position:absolute;left:100px;top:326px;font-size:13px;color:#111}
.social{position:absolute;left:902px;top:318px;display:flex;gap:12px}
.social i{width:32px;height:32px;border:2px solid #111;border-radius:50%;display:block}
</style>
</head>
<body>

<header class="site-header">
  <div class="brand"><span class="brand-mark"></span><span class="brand-name">HARLOW</span></div>
  <div class="top-contact">
    <span class="mail"><span class="dot-icon blue"><svg width="16" height="12" viewBox="0 0 16 12"><rect x="1" y="1" width="14" height="10" fill="none" stroke="#fff" stroke-width="1.6"/><path d="M1 1l7 6 7-6" fill="none" stroke="#fff" stroke-width="1.6"/></svg></span>info@harlowrealestate.com</span>
    <span class="phone"><span class="dot-icon dark"><svg width="16" height="16" viewBox="0 0 24 24"><path fill="#fff" d="M6.6 10.8a15 15 0 006.6 6.6l2.2-2.2c.3-.3.7-.4 1-.2 1.1.4 2.3.6 3.6.6.6 0 1 .4 1 1V20c0 .6-.4 1-1 1A17 17 0 013 4c0-.6.4-1 1-1h3.5c.6 0 1 .4 1 1 0 1.3.2 2.5.6 3.6.1.3 0 .7-.2 1z"/></svg></span>180 047 8815</span>
  </div>
  <nav class="main-nav"><ul><li>Home</li><li>Properties</li><li>Agents</li><li>Gallery</li><li>Blog</li><li>Contact Us</li></ul></nav>
</header>

<section class="hero" role="img" aria-label="Photograph of a warm, furnished living room interior with sofa and wooden shelving">
  <h1 class="hero-title">HARLOW REAL ESTATE MANAGEMENT</h1>
  <p class="hero-sub">" Providing quality commercial and multifamily portfolio management to Landlords, REITs, and financial institutions. "</p>
  <div class="hero-btn">Read More</div>
  <svg class="hero-arrow" style="left:34px" width="30" height="60" viewBox="0 0 30 60"><path d="M26 2L4 30l22 28" fill="none" stroke="#fff" stroke-width="2"/></svg>
  <svg class="hero-arrow" style="right:34px" width="30" height="60" viewBox="0 0 30 60"><path d="M4 2l22 28L4 58" fill="none" stroke="#fff" stroke-width="2"/></svg>
</section>

<div class="cat-shadow"></div>
<article class="cat offices">
  <h3>Offices</h3>
  <p>Nemo enim ipsam voluptatem quia voluptas sit aspernatur autenre odit auton fugiitn sed quia consequuntur magni dolores</p>
  <div class="photo" role="img" aria-label="Photograph of a bright open-plan office with desks" style="background:linear-gradient(180deg,#e8ecef,#b9c2c9 60%,#8e989f)"></div>
</article>
<article class="cat retail">
  <h3>Retail</h3>
  <p>Nemo enim ipsam voluptatem quia voluptas sit aspernatur autenre odit auton fugiitn sed quia consequuntur magni dolores</p>
  <div class="photo" role="img" aria-label="Photograph of a lit retail storefront at dusk" style="background:linear-gradient(180deg,#1d3f7a,#3d5f9a 45%,#c79a5e 75%,#6d5a48)"></div>
</article>
<article class="cat apartments">
  <h3>Apartments</h3>
  <p>Nemo enim ipsam voluptatem quia voluptas sit aspernatur autenre odit auton fugiitn sed quia consequuntur magni dolores</p>
  <div class="photo" role="img" aria-label="Photograph of a modern apartment building with greenery" style="background:linear-gradient(180deg,#cfe0ef,#e3e3df 45%,#7d9a5a 75%,#b4b4ae)"></div>
</article>

<h2 class="section-title" style="top:1088px">About Harlow Real Estate</h2>
<div class="rule" style="left:520px;top:1130px;width:160px"></div>
<p class="about-text">Nemo enim ipsam voluptatem quia voluptas sit aspernatur aut odit aut fugit, sed quia consequuntur magni dolores eos qui ratione voluptatem sequi nesciunt. Neque porro quisquam est, qui dolorem ipsum quia dolor sit amet, consectetur, adipisci velit, sed quia non numquam eius modi tempora incidunt ut labore et dolore magnam aliquam quaerat voluptatem. Ut enim ad minima veniam, quis nostrum</p>

<div class="stats">
  <div class="stat"><svg width="44" height="40" viewBox="0 0 44 40"><rect x="3" y="6" width="38" height="26" rx="3" fill="none" stroke="#0555a3" stroke-width="3"/><rect x="9" y="12" width="11" height="7" fill="#0555a3"/><rect x="24" y="12" width="11" height="7" fill="#0555a3"/><rect x="3" y="22" width="38" height="6" fill="#0555a3"/><path d="M6 32v6M38 32v6" stroke="#0555a3" stroke-width="3"/></svg><div class="label">Bedrooms</div><div class="value">3</div></div>
  <div class="stat"><svg width="44" height="40" viewBox="0 0 44 40"><path d="M4 2v34h36" fill="none" stroke="#0555a3" stroke-width="3"/><path d="M10 8h20v22H10zM10 15h20M10 22h20M17 8v22M24 8v22" fill="none" stroke="#0555a3" stroke-width="2"/><path d="M28 38l12-12v12z" fill="#0555a3"/></svg><div class="label">Square Feet</div><div class="value">2520</div></div>
  <div class="stat"><svg width="44" height="40" viewBox="0 0 44 40"><path d="M8 20V6a4 4 0 018 0" fill="none" stroke="#0555a3" stroke-width="2.5"/><path d="M3 20h38v6a9 9 0 01-9 9H12a9 9 0 01-9-9z" fill="none" stroke="#0555a3" stroke-width="3"/><path d="M10 35l-2 4M34 35l2 4" stroke="#0555a3" stroke-width="2.5"/></svg><div class="label">Baths</div><div class="value">2</div></div>
  <div class="stat"><svg width="44" height="40" viewBox="0 0 44 40"><rect x="5" y="6" width="34" height="32" rx="2" fill="none" stroke="#0555a3" stroke-width="3"/><rect x="5" y="6" width="34" height="8" fill="#0555a3"/><path d="M13 2v8M31 2v8" stroke="#0555a3" stroke-width="3"/><g fill="#0555a3"><rect x="10" y="18" width="5" height="4"/><rect x="19" y="18" width="5" height="4"/><rect x="28" y="18" width="5" height="4"/><rect x="10" y="26" width="5" height="4"/><rect x="19" y="26" width="5" height="4"/><rect x="28" y="26" width="5" height="4"/></g></svg><div class="label">Year Build</div><div class="value">2016</div></div>
  <div class="stat"><svg width="44" height="40" viewBox="0 0 44 40"><path d="M22 2L4 14h36z" fill="#0555a3"/><path d="M10 26l3-8h18l3 8z" fill="#0555a3"/><rect x="8" y="26" width="28" height="8" rx="2" fill="#0555a3"/><rect x="10" y="34" width="5" height="4" fill="#0555a3"/><rect x="29" y="34" width="5" height="4" fill="#0555a3"/><circle cx="13" cy="30" r="2" fill="#fff"/><circle cx="31" cy="30" r="2" fill="#fff"/></svg><div class="label">Car Parking</div><div class="value">1</div></div>
</div>

<section class="services">
  <div class="photo" role="img" aria-label="Photograph of a modern grey living room with sofa and wall-mounted television"></div>
  <h2>OUR SERVICES</h2>
  <div class="srule"></div>
  <p class="intro">Nemo enim ipsam voluptatem quia voluptas sit aspernatur aut odit aut fugit, sed quia consequuntur magni dolores eos qui ratione.</p>
  <div class="service" style="left:627px;top:182px">
    <svg width="46" height="50" viewBox="0 0 46 50"><path d="M16 4h14l-4 8h-6z" fill="#0555a3"/><path d="M18 12h10c8 6 12 14 12 20a12 12 0 01-12 12H18A12 12 0 016 32c0-6 4-14 12-20z" fill="none" stroke="#0555a3" stroke-width="3"/><text x="23" y="36" text-anchor="middle" font-family="Lato,sans-serif" font-weight="700" font-size="15" fill="#0555a3">£</text><rect x="2" y="46" width="42" height="3" fill="#0555a3"/></svg>
    <h4>Financial Institutions</h4><p>Sed ut perspiciatis unde omnis iste error sit voluptatem accusant.</p>
  </div>
  <div class="service" style="left:884px;top:182px">
    <svg width="50" height="50" viewBox="0 0 50 50"><g fill="#0555a3"><rect x="2" y="38" width="7" height="8"/><rect x="12" y="32" width="7" height="14"/><rect x="22" y="26" width="7" height="20"/><rect x="32" y="18" width="7" height="28"/><rect x="42" y="10" width="7" height="36"/></g><path d="M2 30L40 6" stroke="#0555a3" stroke-width="3"/><path d="M34 4h8v8" fill="none" stroke="#0555a3" stroke-width="3"/></svg>
    <h4>Commercial Quality</h4><p>Sed ut perspiciatis unde omnis iste error sit voluptatem accusant.</p>
  </div>
  <div class="service" style="left:627px;top:346px">
    <svg width="54" height="44" viewBox="0 0 54 44"><rect x="6" y="4" width="42" height="28" rx="2" fill="none" stroke="#0555a3" stroke-width="3"/><path d="M2 36h50l-4 5H6z" fill="#0555a3"/><path d="M18 22l9-8 9 8v6H18z" fill="none" stroke="#0555a3" stroke-width="2.5"/></svg>
    <h4>Portfolio Management</h4><p>Sed ut perspiciatis unde omnis iste error sit voluptatem accusant.</p>
  </div>
  <div class="service" style="left:884px;top:346px">
    <svg width="46" height="48" viewBox="0 0 46 48"><path d="M4 20L23 4l19 16v24H4z" fill="none" stroke="#0555a3" stroke-width="3"/><circle cx="23" cy="28" r="9" fill="none" stroke="#0555a3" stroke-width="2.5"/><text x="23" y="33" text-anchor="middle" font-family="Lato,sans-serif" font-weight="700" font-size="13" fill="#0555a3">$</text></svg>
    <h4>Easy To Retail</h4><p>Sed ut perspiciatis unde omnis iste error sit voluptatem accusant.</p>
  </div>
</section>

<h2 class="section-title" style="top:2050px">Our Blog</h2>
<div class="rule" style="left:560px;top:2098px;width:80px"></div>

<article class="post" style="left:100px">
  <div class="photo" role="img" aria-label="Photograph of a pergola-covered outdoor patio with lounge furniture" style="background:linear-gradient(180deg,#5a3a26,#9b7a58 45%,#c9b89a 75%,#5e6a48)"></div>
  <h3 class="accent">Nostrum exercitationem</h3>
  <p>Donec sodales sagittis magna. Sed consequat, leo eget bibendum sodales, augue velit and seltd tasm cursus nunc.</p>
  <div class="btn solid">Read More</div>
</article>
<article class="post" style="left:444px">
  <div class="photo" role="img" aria-label="Photograph of a kitchen with warm wooden cabinets and pendant lights" style="background:linear-gradient(180deg,#8a5a2e,#c07a3e 45%,#d9a86a 70%,#7a4a26)"></div>
  <h3>Perspiciatis unde omnis</h3>
  <p>Donec sodales sagittis magna. Sed consequat, leo eget bibendum sodales, augue velit and seltd tasm cursus nunc.</p>
  <div class="btn">Read More</div>
</article>
<article class="post" style="left:790px">
  <div class="photo" role="img" aria-label="Photograph of an outdoor terrace at dusk with a fire table" style="background:linear-gradient(180deg,#2d4a82,#5070a8 40%,#8a7a6a 70%,#4a3428)"></div>
  <h3>Voluptatem sequi nesciunt</h3>
  <p>Donec sodales sagittis magna. Sed consequat, leo eget bibendum sodales, augue velit and seltd tasm cursus nunc.</p>
  <div class="btn">Read More</div>
</article>

<footer class="site-footer">
  <div class="foot-brand"><span class="brand-mark"></span><span class="brand-name">HARLOW</span></div>
  <div class="foot-contact">
    <span><span class="ring"><svg width="16" height="12" viewBox="0 0 16 12"><rect x="1" y="1" width="14" height="10" fill="none" stroke="#474747" stroke-width="1.6"/><path d="M1 1l7 6 7-6" fill="none" stroke="#474747" stroke-width="1.6"/></svg></span>info@harlowrealestate.com</span>
    <span><span class="ring"><svg width="16" height="16" viewBox="0 0 24 24"><path fill="#474747" d="M6.6 10.8a15 15 0 006.6 6.6l2.2-2.2c.3-.3.7-.4 1-.2 1.1.4 2.3.6 3.6.6.6 0 1 .4 1 1V20c0 .6-.4 1-1 1A17 17 0 013 4c0-.6.4-1 1-1h3.5c.6 0 1 .4 1 1 0 1.3.2 2.5.6 3.6.1.3 0 .7-.2 1z"/></svg></span>180 047 8815</span>
  </div>
  <ul class="foot-nav"><li>Home</li><li>Properties</li><li>Agents</li><li>Gallery</li><li>Blog</li><li>Contact</li></ul>
  <div class="foot-line"></div>
  <p class="copyright">Copyright © 2017 Harlow Real Estate Management. All Right Reserved</p>
  <div class="social"><i></i><i></i><i></i><i></i><i></i></div>
</footer>

</body>
</html>
```